Pricing Brochure Design Project for a Fish Farm

We need a pricing brochure design for a fish farm based in Haiti called Corvel Pisciculture S.A. We raise varies species of tilapia. Each of these species should have a corresponding pricing sheet. Additionally, we should have a pricing sheet for fillets and a separate one for fish carcasses. I have included a draft pricing brochure which contains all of the elements we are looking for as well as our logo.
Target Market(s)
Commercial Buyers (Hotels, Super Markets, Restaurants, etc.)
Industry/Entity Type
Farm
Requirements
Must have
- Please provide a separate sheet for each species of tilapia, one sheet for the tilapia fillets and one sheet for the fish carcasses. If you can find better images, please feel free to replace them.
The information sheet should have an image of the commercial grade cages (similar to the one pictured).
I have not located a suitable image for silver tilapia, but I am having images taken of our stock. If you are unable to locate an image of the silver tilapia, please provide a place holder.
Logo must be included

```html
<!DOCTYPE html>
<html lang="en">
<head>
<meta charset="utf-8">
<title>Corvel Pisciculture – Tilapia Fillets Pricing</title>
<link rel="stylesheet" href="https://fonts.googleapis.com/css2?family=Questrial&display=swap">
<style>
  :root {
    --navy: #123f86;
    --navy-deep: #0b2e6b;
    --green: #3fb54a;
    --green-dark: #2f9a3b;
    --row: #dcdcec;
    --ink: #1a1a1a;
    --white: #ffffff;
  }
  * { box-sizing: border-box; margin: 0; padding: 0; }
  html, body { width: 927px; height: 1200px; overflow: hidden; background: var(--white); }
  body { font-family: "Questrial", "Century Gothic", sans-serif; color: var(--ink); }
  .sheet { position: relative; width: 927px; height: 1200px; overflow: hidden; }

  .wave { position: absolute; left: 0; width: 927px; }
  .wave--top { top: 0; height: 100px; }
  .wave--bottom { bottom: 0; height: 160px; }

  .brand { position: absolute; left: 136px; top: 120px; display: flex; align-items: center; gap: 12px; }
  .brand__mark { width: 34px; height: 34px; border-radius: 50%; background: var(--navy); flex: none; }
  .brand__name { color: var(--navy); font-size: 27px; line-height: 1.05; }

  .title-band { position: absolute; left: 0; top: 250px; width: 927px; height: 121px; display: flex; }
  .title-band__main { width: 500px; background: linear-gradient(90deg, var(--green-dark), var(--green)); position: relative; }
  .title-band__rule { position: absolute; left: 86px; top: 28px; width: 5px; height: 66px; background: var(--white); }
  .title-band__title { position: absolute; left: 106px; top: 32px; color: var(--white); font-size: 47px; font-weight: 400; }
  .title-band__facts { flex: 1; background: linear-gradient(90deg, var(--navy), var(--navy-deep)); padding: 46px 0 0 16px; list-style: none; }
  .title-band__facts li { color: var(--white); font-size: 17px; line-height: 28px; display: flex; align-items: center; gap: 12px; }
  .title-band__facts li::before { content: ""; width: 7px; height: 7px; background: var(--white); flex: none; }

  .product-photo { position: absolute; left: 194px; top: 424px; width: 539px; height: 382px; border: 4px solid var(--navy); background: linear-gradient(135deg, #d8dde2 0%, #eab0a4 35%, #e06a5a 55%, #3a3d42 85%, #23262a 100%); }

  .price-table { position: absolute; left: 94px; top: 853px; width: 742px; border-collapse: collapse; table-layout: fixed; font-size: 13px; }
  .price-table th, .price-table td { border: 2px solid var(--white); text-align: center; }
  .price-table thead th { background: var(--navy); color: var(--white); font-weight: 400; height: 31px; }
  .price-table .col-cut { width: 141px; text-align: left; padding-left: 14px; font-size: 17px; }
  .price-table .group-head { font-size: 16px; letter-spacing: .5px; height: 30px; }
  .price-table tbody td { background: var(--row); height: 37px; font-size: 14px; }
  .price-table tbody td.cut { text-align: left; padding-left: 14px; font-size: 13px; }

  .footer { position: absolute; left: 94px; top: 1139px; display: flex; align-items: center; color: var(--white); font-size: 19px; gap: 12px; }
  .footer__page { font-weight: 400; }
  .footer__sep { opacity: .9; }
  .footer__phone { display: flex; align-items: center; gap: 6px; }
</style>
</head>
<body>
<div class="sheet">
  <svg class="wave wave--top" viewBox="0 0 927 100" preserveAspectRatio="none" aria-hidden="true">
    <path d="M0 0 H927 V78 C820 82 700 70 560 62 C470 56 420 58 380 44 C330 26 260 36 200 48 C120 62 60 66 0 68 Z" fill="var(--white)"/>
    <path d="M300 0 H927 V80 C820 84 700 70 560 64 C470 60 430 56 400 42 C370 28 340 20 300 18 Z" fill="var(--navy)"/>
    <path d="M0 70 C60 68 130 62 200 48 C270 34 330 24 380 42 C420 58 470 60 560 66 C700 74 820 86 927 82" fill="none" stroke="var(--green)" stroke-width="7"/>
  </svg>

  <div class="brand">
    <span class="brand__mark"></span>
    <span class="brand__name">Corvel<br>Pisciculture</span>
  </div>

  <header class="title-band">
    <div class="title-band__main">
      <span class="title-band__rule"></span>
      <h1 class="title-band__title">Tilapia Fillets</h1>
    </div>
    <ul class="title-band__facts">
      <li>5oz to 8oz per fillet</li>
      <li>Min Order for Delivery → 25 lbs</li>
    </ul>
  </header>

  <div class="product-photo" role="img" aria-label="Photo of fresh tilapia fillets laid on crushed ice and a dark slate board"></div>

  <table class="price-table">
    <thead>
      <tr>
        <th class="col-cut" rowspan="2">CUT</th>
        <th class="group-head" colspan="4">WEEKLY PRICING</th>
      </tr>
      <tr>
        <th style="width:132px">$/LB (1–50 lbs)</th>
        <th style="width:170px">$/LB (51 – 150 lbs)</th>
        <th style="width:157px">$/LB (151–250 lbs)</th>
        <th style="width:142px">$/LB (+251 lbs)</th>
      </tr>
    </thead>
    <tbody>
      <tr><td class="cut">Fillet (incl. skin)</td><td>5.00</td><td>4.50</td><td>4.25</td><td>4.00</td></tr>
      <tr><td class="cut">Fillet (skinless)</td><td>5.50</td><td>4.95</td><td>4.68</td><td>4.40</td></tr>
      <tr><td class="cut">Fillet (incl head)</td><td>0.50</td><td>0.45</td><td>0.43</td><td>0.40</td></tr>
    </tbody>
  </table>

  <svg class="wave wave--bottom" viewBox="0 0 927 160" preserveAspectRatio="none" aria-hidden="true">
    <path d="M0 28 C120 22 220 24 300 40 C380 56 420 62 520 62 C680 62 820 60 927 60 V160 H0 Z" fill="var(--navy)"/>
    <path d="M0 22 C120 16 220 18 300 34 C380 50 420 56 520 56 C680 56 820 54 927 54" fill="none" stroke="var(--green)" stroke-width="7"/>
  </svg>

  <footer class="footer">
    <span class="footer__page">6</span>
    <span class="footer__sep">|</span>
    <span class="footer__phone">
      <svg width="22" height="22" viewBox="0 0 24 24" aria-hidden="true"><circle cx="12" cy="12" r="10.5" fill="none" stroke="var(--white)" stroke-width="1.6"/><path d="M9 6.5c-.8.3-1.6 1.3-1.4 2.6.5 3.3 3.6 7 6.8 8.2 1.2.4 2.3-.2 2.7-1l-2-1.9-1.4.8c-1.4-.7-2.8-2.4-3.3-3.9l1.2-1.1z" fill="var(--white)"/></svg>
      509 4712 5580
    </span>
  </footer>
</div>
</body>
</html>
```